KELP Fitness needs an informative flyer

Need collateral flyer for potential clients to understand our fitness training. Should be upscale
LIST ALL RELEVANT INFO. OUR DESIRE IS TO GIVE POTENTAL CLIENTS COLLATERAL THAT WILL INFLUENCE THEM TO CHOOSE KELP OVER OTHER GROUP FITNESS PROGRAMS. =tHE FINAL DESIGN SHOULD COMMUNICATE THE SUCCESS LEVEL OF THE Klp program and how it scientifically makes a difference.
Updates

Target Market(s)

20-45 yr old women and men who are looking to train in a group fitness atmosphere

Industry/Entity Type

Fitness

Requirements
Must have
• the flyer must be eye catching and utilize all prevalent info from website

```html
<!DOCTYPE html>
<html lang="en">
<head>
<meta charset="utf-8">
<title>KELP Fitness – Flyer</title>
<link rel="stylesheet" href="https://fonts.googleapis.com/css2?family=Arimo:ital,wght@0,400;0,700;1,400;1,700&display=swap">
<style>
  :root {
    --ink: #141414;
    --charcoal: #1d1d1d;
    --orange: #ef7d1a;
    --orange-deep: #d3600c;
    --orange-light: #f6a23c;
    --copy-orange: #e58a2a;
    --white: #ffffff;
    --wall: #f1ede8;
  }
  * { margin: 0; padding: 0; box-sizing: border-box; }
  html, body { width: 1200px; height: 3031px; overflow: hidden; background: var(--ink); }
  .flyer {
    position: relative;
    width: 1200px;
    height: 3031px;
    overflow: hidden;
    background: var(--ink);
    font-family: "Arimo", Arial, sans-serif;
  }
  .hero-photo {
    position: absolute;
    left: 0; top: 0;
    width: 1200px; height: 1420px;
    background:
      radial-gradient(ellipse at 18% 10%, var(--wall) 0%, #e4ddd4 22%, transparent 45%),
      linear-gradient(160deg, #d9d2c8 0%, #a79a8d 35%, #7c6b5e 60%, #c8662a 85%, #d97a33 100%);
  }
  .decor {
    position: absolute;
    left: 0; top: 0;
    width: 1200px; height: 3031px;
  }
  .brand {
    position: absolute;
    left: 40px; top: 58px;
    width: 380px;
  }
  .brand-name {
    display: block;
    font-weight: 700;
    font-size: 58px;
    line-height: 1;
    white-space: nowrap;
    color: var(--orange);
  }
  .brand-tagline {
    display: block;
    margin-top: 10px;
    padding-top: 8px;
    border-top: 3px solid var(--ink);
    font-weight: 700;
    font-size: 17px;
    white-space: nowrap;
    color: var(--orange-deep);
  }
  .block {
    position: absolute;
    left: 50px;
    width: 1110px;
    white-space: nowrap;
  }
  .headline {
    top: 1494px;
    font-weight: 700;
    font-style: italic;
    font-size: 46px;
    color: var(--white);
  }
  .body-copy {
    font-size: 28px;
    line-height: 30px;
    color: var(--copy-orange);
  }
  .body-copy span { display: block; }
  .copy-aging { top: 1559px; }
  .copy-science { top: 1787px; }
  .copy-program { top: 2111px; }
  .acronym {
    top: 2372px;
    font-style: italic;
    font-size: 31px;
    color: var(--white);
  }
  .rates {
    top: 2450px;
    font-weight: 700;
    font-style: italic;
    font-size: 58px;
    color: var(--white);
  }
  .cta {
    top: 2552px;
    font-weight: 700;
    font-style: italic;
    font-size: 50px;
    color: var(--orange);
  }
  .phones {
    top: 2650px;
    list-style: none;
  }
  .phones li {
    font-weight: 700;
    font-size: 43px;
    line-height: 62px;
    color: var(--white);
  }
  .website {
    position: absolute;
    left: 375px; top: 2954px;
    font-size: 45px;
    color: var(--ink);
  }
</style>
</head>
<body>
<main class="flyer">
  <div class="hero-photo" role="img" aria-label="Photo of a group fitness class doing assisted pull-ups with resistance bands on a rack, a trainer spotting a member"></div>

  <svg class="decor" viewBox="0 0 1200 3031">
    <defs>
      <linearGradient id="bandOrange" x1="0" y1="0" x2="1" y2="0">
        <stop offset="0" stop-color="#d3600c"/>
        <stop offset="0.5" stop-color="#f6a23c"/>
        <stop offset="1" stop-color="#ef7d1a"/>
      </linearGradient>
      <linearGradient id="circleA" x1="0" y1="0" x2="1" y2="1">
        <stop offset="0" stop-color="#c9b9a8"/>
        <stop offset="1" stop-color="#6b5a4d"/>
      </linearGradient>
      <linearGradient id="circleB" x1="0" y1="0" x2="1" y2="1">
        <stop offset="0" stop-color="#e08a46"/>
        <stop offset="1" stop-color="#5a4538"/>
      </linearGradient>
    </defs>

    <path d="M900 0 C1050 40 1150 120 1200 220 L1200 0 Z" fill="var(--ink)"/>
    <path d="M880 0 C1040 50 1140 130 1200 240 L1200 220 C1150 120 1050 40 900 0 Z" fill="url(#bandOrange)"/>

    <path d="M1200 240 C1150 500 1120 800 1200 1000 Z" fill="var(--ink)"/>
    <path d="M1200 200 C1130 480 1100 800 1200 1030 L1200 1000 C1120 800 1150 500 1200 240 Z" fill="url(#bandOrange)"/>

    <path d="M0 1290 C300 1420 800 1330 1200 1080 L1200 1460 L0 1460 Z" fill="url(#bandOrange)"/>
    <path d="M0 1330 C320 1460 820 1380 1200 1130 L1200 3031 L0 3031 Z" fill="var(--charcoal)"/>

    <path d="M0 2860 C380 2850 850 2760 1200 2650 L1200 3031 L0 3031 Z" fill="var(--orange-deep)"/>
    <path d="M0 2895 C400 2880 870 2800 1200 2700 L1200 3031 L0 3031 Z" fill="url(#bandOrange)"/>

    <circle cx="109" cy="1224" r="104" fill="url(#circleA)" stroke="var(--orange)" stroke-width="8" role="img" aria-label="Photo of class members training with kettlebells"/>
    <circle cx="642" cy="1306" r="115" fill="url(#circleB)" stroke="var(--orange)" stroke-width="8" role="img" aria-label="Photo of members doing stability work with a medicine ball"/>
    <circle cx="1052" cy="1039" r="123" fill="url(#circleB)" stroke="var(--orange)" stroke-width="8" role="img" aria-label="Photo of a group doing resistance band drills"/>
  </svg>

  <header class="brand">
    <span class="brand-name">KELP FITNESS</span>
    <span class="brand-tagline">STRONGER FROM THE CORE OUT</span>
  </header>

  <h1 class="block headline">40 Minutes. 700 Calories</h1>

  <p class="block body-copy copy-aging">
    <span>Designed for all fitness levels. Guaranteed to bring out your “inner</span>
    <span>athlete”. This timed class pushes each individual to new personal best.</span>
    <span>Klp is more than just fitness. Klp combats the effects of aging. Muscle</span>
    <span>mass and motor unit number activation and synchronization are highly</span>
    <span>related to strength ,which unfortunately both decrease with aging.</span>
  </p>

  <p class="block body-copy copy-science">
    <span>High intensity  Resistance-training is the best way to increase muscle</span>
    <span>mass, neural coordination, and strength. Mitochondrial concentration is</span>
    <span>highly  related to endurance capacity in young and old .KELP is proven</span>
    <span>to assist in the replenishment of ATP (Adenosine Triphosphate). ATP is</span>
    <span>often called “the spark of life ”because of its supply of free energy. ATP</span>
    <span>aids in cell efficiency. KELP training consists of the perfect mix of exer-</span>
    <span>cise elements which basically have our clients discovering a so called</span>
    <span>“fountain of youth”.</span>
  </p>

  <p class="block body-copy copy-program">
    <span>Cardio, Strength training, and stability all in one exciting group fitness</span>
    <span>class that is guaranteed to get you the results you are looking for! The</span>
    <span>ORIGINAL and best 40 minute program designed by owner/ trainer Dana</span>
    <span>Reyes to incorporate all aspects of functional and cardiovascular</span>
    <span>training. Designer fitness at its best. In just 3-4 sessions you will notice</span>
    <span>a difference in your body</span>
  </p>

  <p class="block acronym">KELP= Kinetic endurance lifting program</p>
  <p class="block rates">Affordable rates</p>
  <p class="block cta">Book Your Class Today!</p>
  <ul class="block phones">
    <li>(555) 213-0147</li>
    <li>(555) 318-0962</li>
  </ul>

  <footer class="website">www.kelpfitness.com</footer>
</main>
</body>
</html>
```